BrightMold needs an insert advertising two dental laboratory products to go inside a Dental magazine.

We need an insert designed to go inside the Pacific Oral Health Guild bi-monthly magazine. The flyer is to promote two products ( a flexible partial denture and a bitesplint) to dentists. I will provide my company logo and write the script. The brochure needs to be professional looking and be effective.
Regards
Darren Whitcombe

Target Market(s)

Dentists

Industry/Entity Type

Dental

Font styles to use
Serif

Colors
3176b5

Requirements
Must have
• Contemporary, professional, clean lines, images.
Should not have
• Cluttered with too much information

```html
<!DOCTYPE html>
<html lang="en">
<head>
<meta charset="utf-8">
<title>BrightMold – Dental Laboratory Insert</title>
<link rel="stylesheet" href="https://fonts.googleapis.com/css2?family=Exo+2:wght@500;700&family=Lato:wght@400;700&display=swap">
<style>
  :root {
    --brand-blue: #1787bd;
    --brand-blue-deep: #0f6f9e;
    --ink: #1f1f1f;
    --charcoal: #2a2a2a;
    --charcoal-soft: #4a4a4a;
    --paper: #ffffff;
    --paper-shade: #eceef0;
    --stage: #d9dadb;
    --text-grey: #333333;
  }
  * { margin: 0; padding: 0; box-sizing: border-box; }
  html, body { width: 1200px; height: 1200px; overflow: hidden; }
  body {
    background: radial-gradient(circle at 50% 40%, #f1f1f1 0%, var(--stage) 80%);
    font-family: "Lato", Arial, sans-serif;
    position: relative;
  }
  .flyer {
    position: absolute;
    left: 200px; top: 35px;
    width: 800px; height: 1130px;
    background: linear-gradient(180deg, var(--paper) 0%, var(--paper-shade) 100%);
    overflow: hidden;
    box-shadow: 0 10px 30px rgba(0,0,0,.18);
  }
  .flyer-shapes { position: absolute; inset: 0; }
  .brand {
    position: absolute; left: 530px; top: 72px;
    display: flex; align-items: center; gap: 14px;
  }
  .brand-dot { width: 50px; height: 50px; border-radius: 50%; background: var(--brand-blue); }
  .brand-name {
    font-family: "Exo 2", Arial, sans-serif; font-weight: 700;
    font-size: 30px; color: var(--brand-blue); letter-spacing: 1px; line-height: 1;
  }
  .brand-tagline {
    font-size: 10.5px; color: #9a9a9a; letter-spacing: .5px;
    text-transform: uppercase; margin-top: 4px;
  }
  .headline {
    position: absolute; left: 545px; top: 180px;
    font-family: "Exo 2", Arial, sans-serif; font-weight: 700;
    font-size: 74px; line-height: .95; color: var(--paper); letter-spacing: 1px;
  }
  .headline .accent { color: var(--brand-blue); display: block; }
  .product-list {
    position: absolute; left: 420px; top: 530px;
    display: flex; gap: 26px; list-style: none;
    font-size: 19px; color: var(--ink);
  }
  .product-list li { display: flex; align-items: center; gap: 8px; }
  .intro { position: absolute; left: 60px; top: 548px; width: 300px; }
  .intro-title {
    font-family: "Exo 2", Arial, sans-serif; font-weight: 700;
    font-size: 28px; color: var(--brand-blue); letter-spacing: 1px;
  }
  .intro-copy {
    margin-top: 18px; font-size: 15px; line-height: 1.3;
    color: var(--text-grey); text-align: justify;
  }
  .contact { position: absolute; left: 60px; top: 800px; list-style: none; font-size: 15px; color: var(--ink); }
  .contact li { display: flex; align-items: center; gap: 10px; margin-bottom: 9px; }
  .contact svg { flex: none; }
  .web-link {
    position: absolute; left: 50px; top: 905px;
    width: 300px; height: 58px; border-radius: 29px;
    background: var(--brand-blue);
    display: flex; align-items: center; gap: 24px; padding-left: 14px;
    color: var(--paper); font-size: 17px; letter-spacing: 4px; text-decoration: none;
  }
</style>
</head>
<body>
<main class="flyer">
  <svg class="flyer-shapes" width="800" height="1130" viewBox="0 0 800 1130">
    <defs>
      <linearGradient id="panelDark" x1="0" y1="0" x2="1" y2="1">
        <stop offset="0" stop-color="#1a1a1a"/>
        <stop offset="1" stop-color="#474747"/>
      </linearGradient>
      <linearGradient id="portraitTone" x1="0" y1="0" x2="1" y2="1">
        <stop offset="0" stop-color="#f4e6da"/>
        <stop offset=".55" stop-color="#d9b48e"/>
        <stop offset="1" stop-color="#f7f2ee"/>
      </linearGradient>
      <linearGradient id="dentureTone" x1="0" y1="0" x2="1" y2="1">
        <stop offset="0" stop-color="#f7f5f4"/>
        <stop offset=".6" stop-color="#e9b7a6"/>
        <stop offset="1" stop-color="#f2f0ee"/>
      </linearGradient>
      <linearGradient id="modelTone" x1="0" y1="0" x2="1" y2="1">
        <stop offset="0" stop-color="#f3c9a4"/>
        <stop offset="1" stop-color="#e89a6a"/>
      </linearGradient>
    </defs>

    <!-- dark headline panel and stripe -->
    <polygon points="470,0 800,0 800,470 405,470" fill="url(#panelDark)"/>
    <polygon points="402,480 800,480 800,512 398,512" fill="var(--brand-blue)"/>

    <!-- diagonal band -->
    <polygon points="330,500 385,500 665,1130 605,1130" fill="var(--brand-blue)"/>

    <!-- portrait frame -->
    <path d="M-20,-20 L470,-20 L407,430 Q396,520 310,512 L-20,395 Z" fill="var(--brand-blue)"/>
    <path d="M-20,-20 L452,-20 L392,425 Q383,496 312,492 L-20,372 Z" fill="var(--paper)"/>
    <path d="M-20,-20 L444,-20 L386,420 Q377,486 313,482 L-20,362 Z" fill="url(#portraitTone)" role="img" aria-label="Photo of a smiling woman with curly blonde hair"/>

    <!-- bottom band -->
    <rect x="0" y="1052" width="800" height="10" fill="var(--brand-blue)"/>
    <rect x="0" y="1062" width="800" height="68" fill="var(--charcoal)"/>

    <!-- product tiles -->
    <g transform="rotate(14 600 690)">
      <rect x="515" y="605" width="170" height="170" rx="26" fill="var(--ink)"/>
      <rect x="525" y="615" width="150" height="150" rx="18" fill="url(#dentureTone)" role="img" aria-label="Photo of a flexible partial denture with clasp"/>
    </g>
    <g transform="rotate(4 460 805)">
      <rect x="375" y="720" width="170" height="170" rx="26" fill="var(--ink)"/>
      <rect x="385" y="730" width="150" height="150" rx="18" fill="url(#dentureTone)" role="img" aria-label="Photo of a partial denture fitted on a white model"/>
    </g>
    <g transform="rotate(14 520 975)">
      <rect x="440" y="895" width="160" height="160" rx="26" fill="var(--ink)"/>
      <rect x="450" y="905" width="140" height="140" rx="18" fill="url(#modelTone)" role="img" aria-label="Photo of a dental model being finished with a rotary tool"/>
    </g>
  </svg>

  <div class="brand">
    <span class="brand-dot"></span>
    <div>
      <div class="brand-name">BRIGHTMOLD</div>
      <div class="brand-tagline">Innovative laboratory solutions</div>
    </div>
  </div>

  <h1 class="headline">LOREM<span class="accent">IPSUM</span>DOLOR</h1>

  <ul class="product-list">
    <li>
      <svg width="22" height="22" viewBox="0 0 22 22"><circle cx="11" cy="11" r="11" fill="var(--brand-blue)"/><path d="M6 11.5l3.5 3.5 6.5-7" stroke="#fff" stroke-width="2.4" fill="none"/></svg>
      Flexible partial denture
    </li>
    <li>
      <svg width="22" height="22" viewBox="0 0 22 22"><circle cx="11" cy="11" r="11" fill="var(--brand-blue)"/><path d="M6 11.5l3.5 3.5 6.5-7" stroke="#fff" stroke-width="2.4" fill="none"/></svg>
      Bitesplint
    </li>
  </ul>

  <section class="intro">
    <h2 class="intro-title">LOREM IPSUM</h2>
    <p class="intro-copy">Sed tamen est aliquid, quod nobis non liceat, liceat illis. At iam decimum annum in spelunca iacet. Quid, cum fictas fabulas, e quibus utilitas nulla elici notes. Sed tamen est aliquid, quod nobis non liceat, liceat illis. At iam decimum annum in spelunca iacet. Quid, cum fictas fabulas, e quibus utilitas nulla elici e quibus utilitas nobis</p>
  </section>

  <ul class="contact">
    <li>
      <svg width="18" height="18" viewBox="0 0 18 18"><circle cx="9" cy="9" r="9" fill="var(--brand-blue)"/><path d="M6 4.5l2 2-1 1.2c.6 1.3 1.6 2.3 2.9 2.9l1.2-1 2 2-1.3 1.4C8.4 13 5 9.6 4.6 5.8z" fill="#fff"/></svg>
      09 555 0182 | 021 555 0147
    </li>
    <li>
      <svg width="18" height="18" viewBox="0 0 18 18"><circle cx="9" cy="9" r="9" fill="var(--brand-blue)"/><rect x="4.5" y="6" width="9" height="6.5" fill="#fff"/><path d="M4.5 6l4.5 3.6L13.5 6" stroke="var(--brand-blue)" stroke-width="1.2" fill="none"/></svg>
      darren@brightmold.co.nz
    </li>
    <li>
      <svg width="18" height="18" viewBox="0 0 18 18"><circle cx="9" cy="9" r="9" fill="var(--brand-blue)"/><path d="M9 3.8a3.4 3.4 0 0 0-3.4 3.4C5.6 10 9 14.2 9 14.2s3.4-4.2 3.4-7A3.4 3.4 0 0 0 9 3.8z" fill="#fff"/><circle cx="9" cy="7.2" r="1.3" fill="var(--brand-blue)"/></svg>
      14 Harbourview Rd, RD2, Kaiwaka 0573
    </li>
  </ul>

  <a class="web-link" href="#">
    <svg width="34" height="34" viewBox="0 0 34 34"><circle cx="17" cy="17" r="17" fill="#fff"/><path d="M11 23l11-11M14 12h8v8" stroke="var(--ink)" stroke-width="2.6" fill="none"/></svg>
    www.website.com
  </a>
</main>
</body>
</html>
```